Real Estate 24"x24" Sign, Business Card, Letter Head and Envelope

This is a 4 project contest. If we choose a design or designs we like from what you sent we are willing to pay an amount at our discretion for that design even if we don't like all your designs for the 4 projects. Please be creative. Attached are our logo files. Please message us with any questions. Thanks and Good Luck!
Project 1: QLTV Realty 24" x 24" yard sign
We want to use the same blue background in our logo for the sign where the logo in white font will be on. CMYK 100,80,0,0. Attached is a sample a local designer made for you to get an idea what we are looking for. In the sample, the website is way too big and the entire sign is very plain and not attractive looking plus blue color is wrong one. We want the logo on top as large as possible but keeping it proportionate and attractive looking buy not too big that it looks odd. The following information can go in white color background or same blue color background color. Our company colors are blue (as per logo), green (as per logo), and white. "Residential & Commercial" goes under the logo. Under that put our phone number "312-948-6051" as large as possible but still looks good and under that our website in much smaller but readable font "www.qltvrealty.com".
Project 2: Envelope
We have two version of the logo. Use one or both. Whatever looks best in your design. The envelope will be white. We only want on top left corner logo and underneath our mailing address: 5197 Larchmere Ave. Brinmoor, IL 60093-1725. Maybe some creative decorative design at bottom of envelope will look nice
Project 3: Letter Head
We have two version of the logo. Use one or both. Whatever looks best in your design. We want the following information on the top of the letterhead. Logo, address: 5197 Larchmere Ave., Brinmoor, IL 60093-1725, phone: 312-948-6051, fax: 312-682-9307 website www.qltvrealty.com, email: info@qltvrealty.com
Project 4: Business card
Use either logo. We need cards for two individuals. Information for Person 1: Dev Kulkarni, Managing Broker, Phone: 312-948-6051, Email: dev.kulkarni@qltvrealty.com. Person 2: Ajay Kulkarni Broker Phone: 312-519-8263 Email: ajay.kulkarni@qltvrealty.com. Add Address, Fax and website same as above letter head.

```html
<!DOCTYPE html>
<html lang="en">
<head>
<meta charset="utf-8">
<title>QLTV Realty Stationery</title>
<link href="https://fonts.googleapis.com/css2?family=Montserrat:wght@400;500;600;700&display=swap" rel="stylesheet">
<style>
  :root {
    --brand-blue: #1f5494;
    --paper: #ffffff;
    --backdrop: #e8e9eb;
    --ink: #3b4350;
    --ink-soft: #7a8290;
  }
  * { box-sizing: border-box; margin: 0; padding: 0; }
  html, body { width: 1200px; height: 795px; overflow: hidden; }
  body {
    background: var(--backdrop);
    font-family: "Montserrat", sans-serif;
    color: var(--ink);
    position: relative;
  }
  .sheet { position: absolute; background: var(--paper); box-shadow: 0 2px 8px rgba(0,0,0,.12); overflow: hidden; }
  .brand-name { font-family: "Montserrat", sans-serif; font-weight: 700; color: var(--brand-blue); letter-spacing: .02em; white-space: nowrap; }
  .brand-name.on-blue { color: var(--paper); }
  .contact-list { list-style: none; font-size: 8px; line-height: 1.55; color: var(--ink); white-space: nowrap; }
  .contact-list li { display: flex; align-items: center; gap: 5px; }
  .contact-list.right li { justify-content: flex-end; }
  .icon { width: 8px; height: 8px; fill: var(--brand-blue); flex: none; }
  .icon.spacer { visibility: hidden; }

  /* Letterhead */
  .letterhead { left: 60px; top: 30px; width: 340px; height: 481px; border-top: 4px solid var(--brand-blue); }
  .letterhead .brand-name { position: absolute; left: 24px; top: 22px; font-size: 17px; }
  .letterhead .contact-list { position: absolute; right: 22px; top: 22px; font-size: 7.5px; }
  .bottom-band { position: absolute; left: 0; right: 0; bottom: 0; height: 8px; background: var(--brand-blue); }
  .bottom-band::after { content: ""; position: absolute; left: 40%; bottom: 0; width: 36px; height: 12px; background: var(--brand-blue); }

  /* Presentation folder */
  .folder { left: 430px; top: 30px; width: 340px; height: 481px; background: var(--brand-blue); }
  .folder .brand-name { position: absolute; right: 32px; bottom: 36px; font-size: 26px; }

  /* Business cards */
  .card { width: 340px; height: 194px; left: 800px; }
  .card-front { top: 30px; }
  .card-front .brand-name { position: absolute; left: 22px; top: 20px; font-size: 15px; }
  .card-front .person { position: absolute; left: 22px; top: 88px; }
  .person-name { font-size: 15px; font-weight: 700; color: var(--brand-blue); text-transform: uppercase; }
  .person-title { font-size: 9px; font-weight: 500; color: var(--ink-soft); text-transform: uppercase; letter-spacing: .06em; margin-top: 3px; }
  .card-front .contact-list { position: absolute; left: 170px; top: 72px; font-size: 7.5px; }
  .card-front .bottom-band { height: 7px; }
  .card-back { top: 248px; background: var(--brand-blue); }
  .card-back .brand-name { position: absolute; right: 28px; bottom: 26px; font-size: 18px; }

  /* Envelopes */
  .envelope { width: 500px; height: 230px; top: 545px; }
  .envelope-front { left: 80px; }
  .envelope-front .brand-name { position: absolute; left: 26px; top: 22px; font-size: 17px; }
  .envelope-front .return-address { position: absolute; left: 26px; top: 50px; font-size: 8.5px; line-height: 1.5; }
  .envelope-front .bottom-band { height: 9px; }
  .envelope-back { left: 620px; }
  .flap-band { position: absolute; left: 0; right: 0; top: 0; height: 62px; background: var(--brand-blue); border-radius: 0 0 10px 10px; display: flex; align-items: center; justify-content: center; }
  .flap-band .brand-name { font-size: 18px; }
</style>
</head>
<body>
<svg width="0" height="0" style="position:absolute">
  <defs>
    <symbol id="i-pin" viewBox="0 0 10 10"><path d="M5 0a3.5 3.5 0 0 0-3.5 3.5C1.5 6 5 10 5 10s3.5-4 3.5-6.5A3.5 3.5 0 0 0 5 0zm0 5a1.5 1.5 0 1 1 0-3 1.5 1.5 0 0 1 0 3z"/></symbol>
    <symbol id="i-phone" viewBox="0 0 10 10"><path d="M2 0.5l2 2-1 1.3a6 6 0 0 0 3.2 3.2L7.5 6l2 2-1.2 1.5C4 9.5.5 6 .5 1.7z"/></symbol>
    <symbol id="i-fax" viewBox="0 0 10 10"><path d="M2.5 0h5v3h-5zM0 3.5h10v5H8V7H2v1.5H0zM2.5 7.5h5V10h-5z"/></symbol>
    <symbol id="i-web" viewBox="0 0 10 10"><path d="M5 0a5 5 0 1 0 0 10A5 5 0 0 0 5 0zm0 1.2c.6.6 1.1 1.9 1.2 3.2H3.8C3.9 3.1 4.4 1.8 5 1.2zM1.3 5.6h1.4c.1 1 .3 1.9.7 2.6a3.8 3.8 0 0 1-2.1-2.6zm0-1.2a3.8 3.8 0 0 1 2.1-2.6c-.4.7-.6 1.6-.7 2.6zm2.5 1.2h2.4C6.1 6.9 5.6 8.2 5 8.8c-.6-.6-1.1-1.9-1.2-3.2zm2.8 2.6c.4-.7.6-1.6.7-2.6h1.4a3.8 3.8 0 0 1-2.1 2.6zm.7-3.8c-.1-1-.3-1.9-.7-2.6a3.8 3.8 0 0 1 2.1 2.6z"/></symbol>
    <symbol id="i-mail" viewBox="0 0 10 10"><path d="M0 2h10v6H0zm1 1v.3l4 2.5 4-2.5V3z"/></symbol>
  </defs>
</svg>

<section class="sheet letterhead" aria-label="Letterhead">
  <div class="brand-name">QLTV Realty</div>
  <ul class="contact-list right">
    <li>5197 Larchmere Ave.<svg class="icon"><use href="#i-pin"/></svg></li>
    <li>Brinmoor, IL 60093-1725<svg class="icon spacer"><use href="#i-pin"/></svg></li>
    <li>312-948-6051<svg class="icon"><use href="#i-phone"/></svg></li>
    <li>312-682-9307<svg class="icon"><use href="#i-fax"/></svg></li>
    <li>www.qltvrealty.com<svg class="icon"><use href="#i-web"/></svg></li>
    <li>info@qltvrealty.com<svg class="icon"><use href="#i-mail"/></svg></li>
  </ul>
  <div class="bottom-band"></div>
</section>

<section class="sheet folder" aria-label="Presentation folder cover">
  <div class="brand-name on-blue">QLTV Realty</div>
</section>

<section class="sheet card card-front" aria-label="Business card front">
  <div class="brand-name">QLTV Realty</div>
  <div class="person">
    <div class="person-name">Dev Kulkarni</div>
    <div class="person-title">Managing Broker</div>
  </div>
  <ul class="contact-list">
    <li><svg class="icon"><use href="#i-pin"/></svg>5197 Larchmere Ave.</li>
    <li><svg class="icon spacer"><use href="#i-pin"/></svg>Brinmoor, IL 60093-1725</li>
    <li><svg class="icon"><use href="#i-phone"/></svg>312-948-6051</li>
    <li><svg class="icon"><use href="#i-fax"/></svg>312-682-9307</li>
    <li><svg class="icon"><use href="#i-mail"/></svg>dev.kulkarni@qltvrealty.com</li>
    <li><svg class="icon"><use href="#i-web"/></svg>www.qltvrealty.com</li>
  </ul>
  <div class="bottom-band"></div>
</section>

<section class="sheet card card-back" aria-label="Business card back">
  <div class="brand-name on-blue">QLTV Realty</div>
</section>

<section class="sheet envelope envelope-front" aria-label="Envelope front">
  <div class="brand-name">QLTV Realty</div>
  <p class="return-address">5197 Larchmere Ave.<br>Brinmoor, IL 60093-1725</p>
  <div class="bottom-band"></div>
</section>

<section class="sheet envelope envelope-back" aria-label="Envelope back">
  <div class="flap-band"><span class="brand-name on-blue">QLTV Realty</span></div>
</section>
</body>
</html>
```